Website Landing Page for Brightfall Systems

Create a custom designed website landing page for our business. Looking for a professional upscale design that incorporates our logo and logo colors into the theme. I want a standard fixed frame website, not a constant scrolling format that seems to be the trend. To start with I'm looking for more of the graphic design part, maybe a concept or theme, I don't expect to see a finished project. Not interested in generic templates or layouts.

The name of our company is Brightfall Systems and I've attached our logo below. I'd like to have the web page have the same look and feel of our logo, as well as the colors. Our company, Brightfall Systems does system design, installation, and programming, of residential and commercial Audio/Video and Automation systems. We do home theaters, lighting and building automation, video conferencing systems, security camera installations, conference rooms, projectors, distributed audio systems, and similar Technology projects. This will be a professional services/informational website. We will not sell products on this website. This website will be used to advertise our company and communicate our services to prospective customers. Having a well designed, professional and clean website is one way we want to distinguish our company from the competition.

Here are some examples of what I consider a professional well designed website
http://www.qorlamstudio.com/Work/

Last year we had our tradlo store designed (with PixelMarket) and I'm really happy with the way it turned out. You can see it at www.HolvenGearDepot.com I consider this to be a great design and looking for the same level of quality with this new website. However, do not copy or use any part of this design in this new project. This tradlo store is completely separate from our other company Brightfall Systems. I only mention this tradlo store an an example of good work.

Reason: Still going through designs.

Reason: Still working on project and have not had time to review all designs and request revisions.

Reason: Sill going through designs and requesting revisions

Reason: still going through all the submissions we received.

Target Market(s)

People interested in Audio/Video, home theaters, home automation. We do sales, system design, and programming. We typically work on larger projects with both residential and commercial customers.

Industry/Entity Type

Business

Number of Pages Required

1 page

Requirements
Must have
• Great design elements. Please use a white background. I think white goes well with our logo colors.

```html
<!DOCTYPE html>
<html lang="en">
<head>
<meta charset="utf-8">
<title>Brightfall Systems</title>
<link rel="stylesheet" href="https://fonts.googleapis.com/css2?family=Poppins:wght@500;600;700&family=Oswald:wght@500&family=Mulish:wght@400;600&display=swap">
<style>
  :root {
    --blue: #2a78c2;
    --blue-dark: #1f5fa8;
    --green: #5cbf4a;
    --green-light: #6fcf55;
    --teal: #3ab79a;
    --side-bg: #eaeef6;
    --ink: #4a5563;
    --dash: #8a94a3;
    --white: #ffffff;
  }
  * { box-sizing: border-box; margin: 0; padding: 0; }
  html, body { width: 1200px; height: 750px; overflow: hidden; background: var(--white); }
  body { position: relative; font-family: "Mulish", sans-serif; }

  .sidebar {
    position: absolute; left: 0; top: 0; width: 245px; height: 750px;
    background: var(--side-bg); border-right: 5px solid var(--blue);
  }
  .sidebar-wave { position: absolute; left: 0; top: 0; width: 245px; height: 200px; }
  .brand {
    position: absolute; left: 0; top: 30px; width: 245px; text-align: center;
  }
  .brand-dot {
    width: 66px; height: 66px; border-radius: 50%; border: 6px solid var(--blue);
    margin: 0 auto 10px;
  }
  .brand-name {
    font-family: "Oswald", sans-serif; font-weight: 500; font-size: 19px;
    letter-spacing: 1px; color: var(--blue); text-transform: uppercase;
  }
  .nav { position: absolute; left: 25px; top: 242px; width: 178px; list-style: none; }
  .nav li {
    font-size: 12.5px; letter-spacing: .5px; color: var(--ink);
    padding-bottom: 9px; border-bottom: 1px dashed var(--dash);
    margin-bottom: 24px;
  }
  .nav li.active { color: var(--blue); }
  .contact { position: absolute; left: 25px; top: 498px; font-size: 11.5px; color: var(--blue-dark); }
  .contact div { display: flex; align-items: center; gap: 8px; height: 18px; margin-bottom: 15px; }
  .contact svg { flex: none; }
  .rule { position: absolute; left: 25px; width: 178px; border-top: 1px dashed var(--dash); }
  .social-title { position: absolute; left: 25px; top: 604px; font-size: 12.5px; letter-spacing: .5px; color: var(--ink); }
  .social { position: absolute; left: 25px; top: 633px; display: flex; gap: 5px; }
  .social span { width: 25px; height: 25px; border-radius: 50%; background: var(--blue); }
  .social span:nth-child(2) { background: #d9463b; }
  .social span:nth-child(3) { background: #3a8fd0; }
  .social span:nth-child(4) { background: var(--blue-dark); }
  .legal { position: absolute; left: 25px; top: 690px; font-size: 13px; color: var(--ink); }

  .hero {
    position: absolute; left: 250px; top: 0; width: 950px; height: 750px;
    background: linear-gradient(105deg, #3f7aa8 0%, #4a8f9a 35%, #5a9f74 65%, #74b24c 100%);
  }
  .headline { position: absolute; left: 0; top: 190px; width: 950px; text-align: center; }
  .headline span {
    display: inline-block; font-family: "Poppins", sans-serif; font-weight: 600;
    font-size: 41px; line-height: 50px; color: var(--white); border-radius: 20px;
    letter-spacing: .5px;
  }
  .headline .line-one { background: var(--blue-dark); padding: 0 26px; margin-left: 25px; }
  .headline .line-two { background: var(--green); padding: 0 18px; margin-left: -92px; }
  .cta {
    position: absolute; left: 365px; top: 314px; width: 203px; height: 29px;
    background: linear-gradient(var(--green-light), #4bb23a); color: var(--white);
    font-family: "Poppins", sans-serif; font-weight: 600; font-size: 15px;
    text-align: center; line-height: 29px;
  }
  .cards { position: absolute; left: 104px; top: 408px; display: flex; gap: 27px; }
  .card { position: relative; width: 160px; height: 185px; border-radius: 4px; overflow: hidden; }
  .card-photo { position: absolute; inset: 0; }
  .card-band { position: absolute; left: 0; bottom: 0; width: 160px; height: 45px; }
  .card-label {
    position: absolute; left: 0; bottom: 9px; width: 160px; text-align: center;
    font-family: "Poppins", sans-serif; font-weight: 600; font-size: 11px; color: var(--white);
  }
  .chat-tab {
    position: absolute; left: 1168px; top: 275px; width: 32px; height: 161px;
    background: #1d2530; border-radius: 8px 0 0 8px;
  }
  .chat-tab p {
    position: absolute; left: 7px; top: 120px; transform: rotate(-90deg); transform-origin: left top;
    white-space: nowrap; color: var(--white); font-family: Arial, sans-serif; font-size: 12px;
  }
  .chat-tab i { position: absolute; left: 11px; top: 136px; width: 11px; height: 11px; background: var(--white); }
  .copyright {
    position: absolute; right: 33px; top: 713px; font-size: 13px; color: var(--white);
  }
</style>
</head>
<body>
  <aside class="sidebar">
    <svg class="sidebar-wave" viewBox="0 0 245 200" aria-hidden="true">
      <path d="M0 0H245V163C200 180 160 200 110 190 60 180 30 155 0 152Z" fill="#ffffff"/>
    </svg>
    <div class="brand">
      <div class="brand-dot"></div>
      <div class="brand-name">Brightfall Systems</div>
    </div>
    <ul class="nav">
      <li class="active">HOME</li>
      <li>ABOUT US</li>
      <li>SERVICES</li>
      <li>PRODUCTS</li>
      <li>CONTACT US</li>
    </ul>
    <div class="contact">
      <div>
        <svg width="17" height="17" viewBox="0 0 17 17" aria-hidden="true"><circle cx="8.5" cy="8.5" r="7.5" fill="none" stroke="#333" stroke-width="1.3"/><path d="M6 4.5l1.3 2-1 1c.6 1.3 1.5 2.2 2.8 2.8l1-1 2 1.3-.8 1.4C8.2 12 5 8.8 4.6 5.3Z" fill="#333"/></svg>
        555-014-2290
      </div>
      <div>
        <svg width="19" height="17" viewBox="0 0 19 17" aria-hidden="true"><circle cx="9.5" cy="8.5" r="7.5" fill="none" stroke="#333" stroke-width="1.3"/><path d="M4.5 6h10v6h-10Z M4.5 6l5 3.5 5-3.5" fill="none" stroke="#333" stroke-width="1.1"/></svg>
        info@brightfallsystems.com
      </div>
    </div>
    <div class="rule" style="top:588px"></div>
    <div class="social-title">WE ARE SOCIAL</div>
    <div class="social" aria-label="Social links"><span></span><span></span><span></span><span></span></div>
    <div class="rule" style="top:673px"></div>
    <div class="legal">FAQ's &nbsp;| &nbsp;Sitemap &nbsp;| &nbsp;Policy</div>
  </aside>

  <main class="hero" role="img" aria-label="Auditorium with tiered seating and a projection screen, tinted blue to green">
    <div class="headline">
      <span class="line-one">BEST FOR RESIDENTIAL &amp;</span><br>
      <span class="line-two">COMMERCIAL AUTOMATION SYSTEM</span>
    </div>
    <div class="cta">KNOW MORE</div>
    <div class="cards">
      <div class="card">
        <div class="card-photo" role="img" aria-label="Close-up of coloured audio jacks" style="background:linear-gradient(160deg,#8a7a6a,#5a4a40 60%,#b08a60)"></div>
        <svg class="card-band" viewBox="0 0 160 45" aria-hidden="true"><path d="M0 10C50-2 110-2 160 18V45H0Z" fill="#3dba8f"/></svg>
        <div class="card-label">AUDIO</div>
      </div>
      <div class="card">
        <div class="card-photo" role="img" aria-label="Touch panel showing lighting and climate controls" style="background:linear-gradient(160deg,#2a6fd0,#1a4fa8 60%,#123a80)"></div>
        <svg class="card-band" viewBox="0 0 160 45" aria-hidden="true"><path d="M0 10C50-2 110-2 160 18V45H0Z" fill="#3dba8f"/></svg>
        <div class="card-label">VIDEO</div>
      </div>
      <div class="card">
        <div class="card-photo" role="img" aria-label="Control console with screens and dials" style="background:linear-gradient(160deg,#3a4a5a,#1a2530 55%,#2a5a80)"></div>
        <svg class="card-band" viewBox="0 0 160 45" aria-hidden="true"><path d="M0 10C50-2 110-2 160 18V45H0Z" fill="#3dba8f"/></svg>
        <div class="card-label">AUTOMATION</div>
      </div>
      <div class="card">
        <div class="card-photo" role="img" aria-label="Network cables in blue light" style="background:linear-gradient(160deg,#5ab0d8,#2a80b0 55%,#a8d8e8)"></div>
        <svg class="card-band" viewBox="0 0 160 45" aria-hidden="true"><path d="M0 10C50-2 110-2 160 18V45H0Z" fill="#3dba8f"/></svg>
        <div class="card-label">NETWORKS</div>
      </div>
    </div>
    <div class="copyright">Copyright © 2017, Brightfall Systems. All Rights Reserved</div>
  </main>

  <div class="chat-tab"><p>Leave a message!</p><i></i></div>
</body>
</html>
```